Professional business cards for real estate development company

I need business cards for my new real estate development company. The company, "KORVA" is a real estate development, investment, and advisory firm with a focus on multifamily, office, and mixed-use projects across primary and secondary markets in the Southeast United States.

Style preference is modern

Industry/Entity Type

Real Estate Development

Contact Information for Business Card

The business cards need to include:
Name
Title
Mailing Address
Phone Number
Web Address

Logo is attached. I would like white to be the primary color with incorporation of the company colors: #232D3A and #B5A451

Font styles to use
Other font styles liked:
• Montserrat, Avenir

Requirements
Must have
• Company Logo. No need to include the company name since the name is in the logo.
Should not have
• No line type designs

```html
<!DOCTYPE html>
<html lang="en">
<head>
<meta charset="utf-8">
<title>KORVA Business Cards</title>
<link href="https://fonts.googleapis.com/css2?family=Montserrat:wght@500;600;800&display=swap" rel="stylesheet">
<style>
  :root {
    --navy: #232D3A;
    --navy-light: #3a4554;
    --gold: #B5A451;
    --white: #ffffff;
    --paper: #e4e4e4;
    --ink: #2a313b;
  }
  * { margin: 0; padding: 0; box-sizing: border-box; }
  html, body { width: 1200px; height: 982px; overflow: hidden; }
  body {
    background: var(--paper);
    font-family: "Montserrat", Arial, sans-serif;
    position: relative;
  }
  .card {
    position: absolute;
    top: 206px;
    width: 330px;
    height: 570px;
    overflow: hidden;
    box-shadow: 0 10px 28px rgba(0,0,0,0.18);
  }
  .card--front { left: 205px; background: var(--white); }
  .card--back {
    left: 665px;
    background: radial-gradient(ellipse at 50% 48%, var(--navy-light) 0%, var(--navy) 70%);
  }
  .brand {
    position: absolute;
    left: 0; right: 0;
    display: flex;
    align-items: center;
    justify-content: center;
    gap: 12px;
    font-weight: 600;
    letter-spacing: 6px;
  }
  .brand__square { width: 16px; height: 16px; }
  .card--front .brand { top: 100px; font-size: 46px; color: var(--navy); }
  .card--front .brand__square { background: var(--navy); }
  .card--back .brand { top: 232px; font-size: 54px; color: var(--white); }
  .card--back .brand__square { background: var(--white); }

  .name-band {
    position: absolute;
    top: 214px; left: 0; right: 0;
    height: 86px;
    background: var(--navy);
    text-align: center;
    padding-top: 20px;
  }
  .name-band__name {
    font-weight: 800; font-size: 25px; color: var(--gold); letter-spacing: 0.5px;
  }
  .name-band__title {
    font-weight: 500; font-size: 12.5px; color: var(--white); letter-spacing: 0.8px; margin-top: 2px;
  }
  .divider {
    position: absolute; left: 52px; right: 52px; height: 20px;
    display: flex; align-items: center; justify-content: center; gap: 4px;
  }
  .divider::before, .divider::after {
    content: ""; flex: 1; height: 1.5px; background: var(--gold);
  }
  .divider--contact { top: 334px; }
  .divider--address { top: 458px; }
  .divider svg { width: 20px; height: 20px; display: block; }
  .contact {
    position: absolute; left: 0; right: 0; top: 366px;
    text-align: center; font-weight: 500; font-size: 14px; line-height: 26px; color: var(--ink);
  }
  .address {
    position: absolute; left: 0; right: 0; top: 492px;
    text-align: center; font-weight: 500; font-size: 13.5px; line-height: 22px; color: var(--ink);
  }
  .foot-band {
    position: absolute; left: 0; right: 0; bottom: 0; height: 14px; background: var(--navy);
  }
  .back-web {
    position: absolute; left: 0; right: 0; bottom: 66px;
    text-align: center; font-weight: 500; font-size: 15px; color: var(--gold); letter-spacing: 0.4px;
  }
</style>
</head>
<body>
  <section class="card card--front">
    <div class="brand"><span class="brand__square"></span>KORVA</div>
    <div class="name-band">
      <div class="name-band__name">DANIEL REYES</div>
      <div class="name-band__title">MANAGING DIRECTOR</div>
    </div>
    <div class="divider divider--contact">
      <svg viewBox="0 0 20 20" aria-hidden="true"><polygon points="10,1 18,5.5 18,14.5 10,19 2,14.5 2,5.5" fill="#B5A451"/><path d="M7 6.5c.5-.5 1-.5 1.3 0l.8 1.3c.2.4 0 .7-.3 1l-.4.3c.4.9 1.1 1.6 2 2l.3-.4c.3-.3.6-.5 1-.3l1.3.8c.5.3.5.8 0 1.3l-.6.6c-2.5.2-5.8-3.1-5.6-5.6z" fill="#fff"/></svg>
      <svg viewBox="0 0 20 20" aria-hidden="true"><polygon points="10,1 18,5.5 18,14.5 10,19 2,14.5 2,5.5" fill="#B5A451"/><rect x="5.5" y="6.8" width="9" height="6.4" fill="none" stroke="#fff" stroke-width="1.1"/><path d="M5.5 6.8l4.5 3.6 4.5-3.6" fill="none" stroke="#fff" stroke-width="1.1"/></svg>
      <svg viewBox="0 0 20 20" aria-hidden="true"><polygon points="10,1 18,5.5 18,14.5 10,19 2,14.5 2,5.5" fill="#B5A451"/><circle cx="10" cy="10" r="4.3" fill="none" stroke="#fff" stroke-width="1.1"/><path d="M5.7 10h8.6M10 5.7c-2 2.4-2 6.2 0 8.6M10 5.7c2 2.4 2 6.2 0 8.6" fill="none" stroke="#fff" stroke-width="0.9"/></svg>
    </div>
    <div class="contact">
      <p>555-0142-7788</p>
      <p>hello@korvadev.com</p>
      <p>www.korvadev.com</p>
    </div>
    <div class="divider divider--address">
      <svg viewBox="0 0 20 20" aria-hidden="true"><polygon points="10,1 18,5.5 18,14.5 10,19 2,14.5 2,5.5" fill="#B5A451"/><path d="M10 14.5s-3.5-3.3-3.5-5.6a3.5 3.5 0 0 1 7 0c0 2.3-3.5 5.6-3.5 5.6z" fill="#fff"/><circle cx="10" cy="8.9" r="1.3" fill="#B5A451"/></svg>
    </div>
    <div class="address">
      <p>418 Magnolia Avenue,</p>
      <p>Charlotte, NC - 28202</p>
    </div>
    <div class="foot-band"></div>
  </section>

  <section class="card card--back">
    <div class="brand"><span class="brand__square"></span>KORVA</div>
    <div class="back-web">www.korvadev.com</div>
  </section>
</body>
</html>
```